Web Design Project - grocery store

A small grocery store in Germany selling food and cloths wants his own web site. They want to set up a new webpage as the old isn't up2date anymore. The page shall cover the consumer usecases: I as a consumer wants to INFORM me, ORDER stuff, check COUPONs, ADVERTISE, LIKE the stuff.
* INFORM: The page shall show the current offers for food (basic, organic, whole, butcher, bakery) and cloths (different brands for men, women and kids). There then the latest news and offers are placed.
* ORDER: The page shall list a set of affiliates where the consumer can order stuff (and if available collect in the store). These are basically German affiliates like Brunvel, LORA foto shop or some local insurance services. The page shall show their content and in case the consumer orders then interact with their system having an merchant ID so that the purchase can be booked in the merchant account for its bonus payments. Also, it could be that the page just present the link to the affiliate page and the consumer then interact there.
* COUPONs: The page shall connect to a coupon service and present the current coupons available. For purchasing the consumer uses a link and the values are booked then in the external service's system.
* ADVERTISE: The page shall offer a function where the consumer can place an offer. Also, there are some Consumer2Consumer pages available where the data could be grabbed and presented. Would be then a web service to integrate.
* LIKE: The page shall list the Chatterloop interaction there. The consumer can like and place comments at the wall.
Industry/Entity Type
Grocery Store
Look and feel
Each slider illustrates characteristics of the customer's brand and the style your logo design should communicate.

```html
<!DOCTYPE html>
<html lang="en">
<head>
<meta charset="utf-8">
<title>Lindenhof – Grocery Store</title>
<link rel="stylesheet" href="https://fonts.googleapis.com/css2?family=Open+Sans:wght@400;600&family=Parisienne&family=Pinyon+Script&display=swap">
<style>
:root{
  --ink:#222;
  --muted:#444;
  --orange:#f18a1c;
  --orange-dark:#e57710;
  --frame:#2b3038;
  --tan:#d5b995;
  --mustard:#dba231;
  --lime:#abc24b;
  --crimson:#b42c2c;
  --social-blue:#3b5b98;
  --line:#555;
  --page:#fff;
}
*{margin:0;padding:0;box-sizing:border-box}
html,body{width:1000px;height:1200px;overflow:hidden;background:var(--page)}
body{position:relative;font-family:"Open Sans",Arial,sans-serif;color:var(--ink)}
.abs{position:absolute}

.brand{left:92px;top:24px;font-size:50px;font-weight:400;color:var(--muted);letter-spacing:-1px;line-height:1}
.cart{left:626px;top:4px;display:flex;align-items:center;gap:6px;color:var(--orange);font-size:14px}
.account{left:795px;top:0;width:129px;height:23px;background:var(--orange);border-radius:0 0 6px 6px;font-size:11px;color:#222;display:flex;align-items:center;justify-content:center;gap:10px}
.main-nav{top:0;left:398px;height:86px}
.main-nav a{position:absolute;top:47px;font-size:15px;color:var(--ink);text-decoration:none;white-space:nowrap}
.main-nav .home-tab{top:0;left:0;width:86px;height:86px;border-radius:0 0 5px 5px;background:linear-gradient(#f7a74e,var(--orange-dark) 60%,#f4a04a);color:#fff;text-align:center;padding-top:47px}
.main-nav .current{color:var(--orange)}

.slider{left:69px;top:100px;width:862px;height:400px;background:var(--frame);border-radius:3px}
.slide{left:16px;top:14px;width:830px;height:371px;background:radial-gradient(ellipse at 55% 45%,#d59a58 0%,#b8743a 45%,#8c5a32 75%,#e8e3de 100%)}
.caption{left:130px;top:316px;width:595px;height:62px;background:rgba(244,135,20,.92);padding:6px 32px;color:#fff}
.caption h2{font-size:15.5px;font-weight:400;line-height:22px;white-space:nowrap}
.caption p{font-size:9.5px;color:#3a2410;line-height:12px;font-weight:600;max-width:420px}
.slider-shadow{left:90px;top:498px;width:820px;height:40px;background:radial-gradient(ellipse at 50% 0,rgba(0,0,0,.45),rgba(0,0,0,0) 70%)}
.pager{left:412px;top:518px;width:181px;height:31px;border:2px solid #c6d3e0;border-radius:5px;background:linear-gradient(#fff,#eef1f4);display:flex;align-items:center}
.pager .arrows{width:52px;height:100%;border-right:1px solid #c6d3e0;display:flex;align-items:center;justify-content:center;gap:6px}
.pager .dots{display:flex;gap:9px;padding-left:11px}
.pager .dots i{width:9px;height:9px;border-radius:50%;background:#a9b0b8}
.pager .dots i.on{background:#222}

.welcome h1{position:absolute;left:80px;top:562px;font-family:"Pinyon Script",cursive;font-weight:400;font-size:28px;color:#333;white-space:nowrap}
.welcome h1 span{color:var(--orange)}
.welcome p{position:absolute;left:80px;top:606px;width:630px;font-size:11.5px;line-height:24px;letter-spacing:-.3px;color:#222}
.welcome p span{display:block;white-space:nowrap}
.welcome-photo{left:706px;top:564px;width:215px;height:173px;border:1px solid #ccc;background:linear-gradient(135deg,#ece8e2,#d8d4cf 60%,#c9c4be)}

.product{top:745px;width:205px;height:320px}
.product h3{position:absolute;left:14px;top:4px;font-family:"Parisienne",cursive;font-weight:400;font-size:28px;line-height:42px;color:#222}
.product .heart{position:absolute;right:14px;top:2px}
.product .photo{position:absolute;left:6px;top:89px;width:192px;height:140px;border-radius:8px}
.product .blurb{position:absolute;left:0;width:100%;top:237px;text-align:center;font-size:12.5px;color:#111}
.product .price{position:absolute;left:12px;top:260px;font-family:"Parisienne",cursive;font-size:25px;color:#fff;white-space:nowrap}
.product .add{position:absolute;top:299px;width:136px;height:30px;border-radius:6px;color:#fff;font-size:14px;text-align:center;line-height:28px}
.p1{left:80px;background:var(--tan)} .p1 .photo{background:linear-gradient(135deg,#f4efe8,#c88b3e 55%,#a3662a)} .p1 .add{left:30px;background:linear-gradient(#b49c7a,#7e6545)}
.p2{left:292px;background:var(--mustard)} .p2 .photo{background:linear-gradient(135deg,#6b5a3a,#a88a5c 45%,#4f7a2a)} .p2 .add{left:35px;background:linear-gradient(#f4c34a,#d08a10)}
.p3{left:504px;background:var(--lime)} .p3 .photo{background:linear-gradient(135deg,#f2f0ee,#e8d7c4 50%,#c25a52)} .p3 .add{left:38px;background:linear-gradient(#9cc63a,#5f8a12)}
.p4{left:716px;background:var(--crimson)} .p4 .photo{background:linear-gradient(135deg,#d7dcdf,#8a5a34 50%,#e9eaea)} .p4 .add{left:34px;background:linear-gradient(#d0323a,#8c1414)}

.social-tab{left:962px;top:553px;width:38px;height:210px;background:var(--social-blue);border-radius:6px 0 0 6px}
.social-tab span{position:absolute;left:7px;top:150px;transform:rotate(-90deg);transform-origin:0 0;color:#fff;font-size:16px;white-space:nowrap}
.social-dot{left:954px;top:717px;width:34px;height:34px;border-radius:50%;background:var(--social-blue);border:3px solid #fff;box-shadow:0 0 3px rgba(0,0,0,.4)}

.footer-nav{top:1104px;left:0;width:1000px;font-size:15px}
.footer-nav a{position:absolute;color:var(--ink);text-decoration:none;white-space:nowrap}
.footer-rule{left:75px;top:1138px;width:849px;height:1px;background:var(--line)}
.copyright{left:385px;top:1155px;font-size:11px;color:#222}
.social{top:1144px;width:28px;height:28px;border-radius:4px}
</style>
</head>
<body>

<div class="abs brand">Lindenhof</div>

<div class="abs cart">
  <svg width="32" height="28" viewBox="0 0 32 28" aria-hidden="true"><path d="M1 3h5l4 15h16l3-10H8" fill="none" stroke="#222" stroke-width="2.2" stroke-linejoin="round"/><circle cx="12" cy="23" r="2.3" fill="#222"/><circle cx="24" cy="23" r="2.3" fill="#222"/></svg>
  <span>My cart 0 item(s)</span>
</div>
<div class="abs account"><span>Login</span><span>|</span><span>Register</span></div>

<nav class="abs main-nav">
  <a class="home-tab" style="left:0">Home</a>
  <a style="left:100px">Inform</a>
  <a class="current" style="left:185px">Order</a>
  <a style="left:267px">Coupons</a>
  <a style="left:368px">Advertise</a>
  <a style="left:455px">Contact us</a>
</nav>

<section class="abs slider">
  <div class="abs slide" role="img" aria-label="Close-up photo of golden fried chicken pieces on a white plate"></div>
  <div class="abs caption">
    <h2>Contrary to popular belief, Lorem Ipsum is not simply random text.</h2>
    <p>All the Lorem Ipsum generators on the Internet tend to repeat predefined chunks as necessary, making this the first true generator on the Internet</p>
  </div>
</section>
<div class="abs slider-shadow"></div>
<div class="abs pager">
  <div class="arrows">
    <svg width="8" height="12" viewBox="0 0 8 12"><path d="M7 1L2 6l5 5" fill="none" stroke="#222" stroke-width="2.5"/></svg>
    <svg width="8" height="12" viewBox="0 0 8 12"><path d="M1 1l5 5-5 5" fill="none" stroke="#999" stroke-width="2"/></svg>
  </div>
  <div class="dots"><i></i><i></i><i class="on"></i><i></i><i></i><i></i></div>
</div>

<section class="welcome">
  <h1>Welcome to <span>L</span>indenhof</h1>
  <p>
    <span>On the other hand, we denounce with righteous indignation and dislike men who are so beguiled and demorali-</span>
    <span>zed by the charms of pleasure of the moment, so blinded by desire, that they cannot foresee the pain and trou-</span>
    <span>ble that are bound to ensue; and equal blame belongs to those who fail in their duty through weakness of will,</span>
    <span>which is the same as saying through shrinking from toil and pain. These cases are perfectly simple and easy to</span>
    <span>distinguish. In a free hour, when our power of choice is untrammelled and when nothing prevents</span>
  </p>
</section>
<div class="abs welcome-photo" role="img" aria-label="Photo of sushi rolls and fresh vegetables on a white square plate"></div>

<article class="abs product p1">
  <h3>frozen<br>chicken</h3>
  <svg class="heart" width="52" height="44" viewBox="0 0 52 44" aria-hidden="true"><path d="M26 42C8 30 4 20 10 12c5-6 13-4 16 3 3-7 11-9 16-3 6 8 2 18-16 30z" fill="#fff"/></svg>
  <div class="photo" role="img" aria-label="Photo of breaded chicken nuggets with a dish of ketchup"></div>
  <div class="blurb">loves or pursues or desires</div>
  <div class="price">Price &nbsp;: $ 250</div>
  <div class="add">Add to Cart</div>
</article>
<article class="abs product p2">
  <h3>mutton<br>packets</h3>
  <svg class="heart" width="52" height="44" viewBox="0 0 52 44" aria-hidden="true"><path d="M26 42C8 30 4 20 10 12c5-6 13-4 16 3 3-7 11-9 16-3 6 8 2 18-16 30z" fill="#fff"/></svg>
  <div class="photo" role="img" aria-label="Photo of stir-fried mutton with green peppers and onion"></div>
  <div class="blurb">loves or pursues or desires</div>
  <div class="price">Price &nbsp;: $ 250</div>
  <div class="add">Add to Cart</div>
</article>
<article class="abs product p3">
  <h3>bakery<br>cakes</h3>
  <svg class="heart" width="52" height="44" viewBox="0 0 52 44" aria-hidden="true"><path d="M26 42C8 30 4 20 10 12c5-6 13-4 16 3 3-7 11-9 16-3 6 8 2 18-16 30z" fill="#fff"/></svg>
  <div class="photo" role="img" aria-label="Photo of layered cream cake slices topped with strawberries"></div>
  <div class="blurb">loves or pursues or desires</div>
  <div class="price">Price &nbsp;: $ 250</div>
  <div class="add">Add to Cart</div>
</article>
<article class="abs product p4">
  <h3>bakery<br>pastries</h3>
  <svg class="heart" width="52" height="44" viewBox="0 0 52 44" aria-hidden="true"><path d="M26 42C8 30 4 20 10 12c5-6 13-4 16 3 3-7 11-9 16-3 6 8 2 18-16 30z" fill="#fff"/></svg>
  <div class="photo" role="img" aria-label="Photo of a nut-topped pastry swirl on a white plate"></div>
  <div class="blurb">loves or pursues or desires</div>
  <div class="price">Price &nbsp;: $ 250</div>
  <div class="add">Add to Cart</div>
</article>

<div class="abs social-tab"><span>chatterloop like</span></div>
<div class="abs social-dot"></div>

<nav class="abs footer-nav">
  <a style="left:142px">Home</a>
  <a style="left:217px">Inform</a>
  <a style="left:302px">Order</a>
  <a style="left:384px">Coupons</a>
  <a style="left:486px">Advertise</a>
  <a style="left:589px">Login</a>
  <a style="left:668px">My cart</a>
  <a style="left:757px">Contact us</a>
</nav>
<div class="abs footer-rule"></div>
<div class="abs copyright">Copyright © 2011 .www.lindenhof-markt.de</div>
<div class="abs social" style="left:812px;background:#3cb0e0" aria-label="Skylark"></div>
<div class="abs social" style="left:851px;background:#f07a1a" aria-label="News feed"></div>
<div class="abs social" style="left:892px;background:var(--social-blue)" aria-label="Chatterloop"></div>

</body>
</html>
```